Business Card Design Project

We would like a business card designed for our Tiny Acorns Club. Although we do want to be creative, it is important for us to maintain branding, therefore most of the design will be copied from our website.
We do want people to know what it is all about, so we included some of the wording. However we rely heavily on your advice and if you think it is better without then as long as design is good we are willing to consider it.
All designs submitted must follow print-ready design rules. Use only CMYK colours
Target Market(s)
Mothers and mothers-to-be
Industry/Entity Type
Business
Look and feel
Each slider illustrates characteristics of the customer's brand and the style your logo design should communicate.

```html
<!DOCTYPE html>
<html lang="en">
<head>
<meta charset="utf-8">
<title>Tiny Acorns Club – Business Card</title>
<link rel="stylesheet" href="https://fonts.googleapis.com/css2?family=Cardo:wght@400;700&display=swap">
<style>
  :root {
    --backdrop: #e8e5e0;
    --card-paper: #f7f5f0;
    --orange-light: #f6b21c;
    --orange-mid: #eea31a;
    --orange-deep: #e48f16;
    --title-white: #ffffff;
    --ink: #4a3a1c;
    --shadow: rgba(40, 30, 15, 0.22);
  }
  * { margin: 0; padding: 0; box-sizing: border-box; }
  html, body {
    width: 1200px;
    height: 1000px;
    overflow: hidden;
  }
  body {
    background: var(--backdrop);
    font-family: "Cardo", "Times New Roman", serif;
    position: relative;
  }
  .business-card {
    position: absolute;
    left: 380px;
    top: 120px;
    width: 440px;
    height: 760px;
    border-radius: 28px;
    background: var(--card-paper);
    overflow: hidden;
    box-shadow: 0 10px 30px var(--shadow);
  }
  .brand-band {
    position: absolute;
    left: 0; top: 0;
    width: 440px;
    height: 370px;
    background:
      repeating-linear-gradient(90deg,
        rgba(255,255,255,0.07) 0 22px,
        rgba(0,0,0,0.035) 22px 44px),
      radial-gradient(ellipse at 55% 35%, var(--orange-light) 0%, var(--orange-mid) 55%, var(--orange-deep) 100%);
  }
  .band-edge {
    position: absolute;
    left: 0;
    top: 370px;
    width: 440px;
    height: 9px;
    display: block;
  }
  .club-name {
    position: absolute;
    left: 0; top: 72px;
    width: 440px;
    text-align: center;
    color: var(--title-white);
    font-weight: 400;
    font-size: 66px;
    line-height: 70px;
    letter-spacing: 0.5px;
  }
  .member-name {
    position: absolute;
    left: 0; top: 440px;
    width: 440px;
    text-align: center;
    color: var(--ink);
    font-weight: 400;
    font-size: 38px;
  }
  .contact-list {
    position: absolute;
    left: 0; top: 538px;
    width: 440px;
    list-style: none;
    text-align: center;
    color: var(--ink);
    font-size: 19px;
    line-height: 40px;
  }
  .contact-list .label { font-weight: 700; }
  .website {
    position: absolute;
    left: 0; top: 680px;
    width: 440px;
    text-align: center;
    color: var(--ink);
    font-weight: 700;
    font-size: 21px;
  }
</style>
</head>
<body>
  <article class="business-card">
    <header class="brand-band">
      <h1 class="club-name">Tiny<br>Acorns<br>Club</h1>
    </header>
    <svg class="band-edge" viewBox="0 0 440 9" preserveAspectRatio="none" aria-hidden="true">
      <defs>
        <pattern id="zigzag-teeth" width="11" height="9" patternUnits="userSpaceOnUse">
          <polygon points="0,0 11,0 5.5,9" fill="#e8a01a"/>
        </pattern>
      </defs>
      <rect width="440" height="9" fill="url(#zigzag-teeth)"/>
    </svg>

    <h2 class="member-name">Jane Doe</h2>

    <ul class="contact-list">
      <li><span class="label">Tel:</span> 031 555 0199</li>
      <li><span class="label">Mobile:</span> 031 555 0199</li>
      <li><span class="label">Email:</span> info@tinyacornsclub.com</li>
    </ul>

    <p class="website">www.tinyacornsclub.com</p>
  </article>
</body>
</html>
```